Ortel Ridge Wine Club-The Velvet Roll

We are a new aspirational brand of fine Tasmania Wine. We need a commitment club poster which appeals to the ego.We have one opportunity to get customers to sign up and that is when they visit at the cellar door. This club is the core of our business.

The brand is a clean, pure , simple brand, black and white very sophiscated.
This is a top end product.

Our Commitment Club is named The Velvet Roll which is a play on words. Tradionally the velvet roll is a list of people that you dont want to do business with. So we are turning this on its had.

You need to make this poster sharp, desirable, possibly sexy but masculine. Im thinking Conrad Vale . It doesnt matter the client will be 40 up fashion consious looking for something new , exclusive , something there peers don't have.

I dont like busy! make it clean clear and basically undeniable. The client must not be able to resist the offer.

www.ortelridge-example.com.au

Target Market(s)

Appreciator 40-60 male wants to be recognised fashion consious sophiscated has money and wants to part of something exclusive.

A feeling that you are part of something that only a few are. Exclusive

Maybe an imagine of beautiful people 30/40ish I want to be drinking Ortel Wine / in the velvet roll

Industry/Entity Type

Fashion

Requirements
Must have
• Ortel Ridge Logo
ORTEL Bottles images

We produce only 1600 cases of wine each vintage. Therefore we have limited membership 001-999 for our club.
Award Winning Wines available exclusively from us.

Gold Member
We will reserve 2 cases of our limited vintage, to be delivered to you in May and Oct.
Single varietal or mixed cases. You receive a 15% discount.

Silver Member
We will reserve 1 case of our limited vintage to be delivered to you 6 bottles in May and 6 in Oct.
Single varietal or mixed cases. You receive a 10% discount.

To you exclusively from us not, available from any other retailers.

You will be invited to Velvet Roll Only Events and Tastings.
You will get preferential access to new and limited releases.
Members will be entered in a bi annual draw to win a 2 night stay here at the Ortel Weavers Lodge on the Freycinet Coast Tasmania.

Should not have
• VIP stamps,gimacs, anything that cheapens our brand.

We do not like busy posters please have white space

```html
<!DOCTYPE html>
<html lang="en">
<head>
<meta charset="utf-8">
<title>Ortel Ridge Wine Club – The Velvet Roll</title>
<link rel="stylesheet" href="https://fonts.googleapis.com/css2?family=Archivo+Black&family=Arimo:ital,wght@0,400;0,700;1,700&family=Great+Vibes&family=Montserrat:wght@300;400;500&display=swap">
<style>
  :root {
    --ink: #111111;
    --paper: #f4f3ef;
    --cream: #efece2;
    --band: #050505;
    --white: #ffffff;
    --gold-light: #fff4c2;
    --gold: #e2b64a;
    --gold-deep: #9c6f14;
    --photo-light: #d9d9d9;
    --photo-dark: #1b1b1b;
  }
  * { margin: 0; padding: 0; box-sizing: border-box; }
  html, body { width: 960px; height: 1200px; overflow: hidden; background: var(--paper); }
  .poster {
    position: relative; width: 960px; height: 1200px; overflow: hidden;
    font-family: "Montserrat", sans-serif; color: var(--ink);
  }

  /* Hero */
  .hero {
    position: absolute; left: 0; top: 0; width: 960px; height: 461px;
    background: radial-gradient(ellipse at center, #ffffff 0%, #ecebe8 70%, #dcdbd8 100%);
  }
  .hero__waiter {
    position: absolute; top: 0; width: 290px; height: 461px;
    background: linear-gradient(90deg, var(--photo-light) 0%, var(--photo-dark) 25%, #f2f2f2 42%, #f6f6f6 58%, var(--photo-dark) 75%, var(--photo-light) 100%);
  }
  .hero__waiter--left { left: 0; }
  .hero__waiter--right { right: 0; width: 268px; }
  .brand {
    position: absolute; left: 0; right: 0; top: 92px; text-align: center;
    font-family: "Montserrat", sans-serif; font-weight: 300; font-size: 62px;
    letter-spacing: 4px; color: var(--ink);
  }
  .brand__mark {
    display: inline-block; width: 12px; height: 12px; border-radius: 50%;
    background: var(--ink); vertical-align: middle; margin-right: 14px;
  }
  .hero__invite {
    position: absolute; left: 0; right: 0; top: 246px; text-align: center;
    font-family: "Arimo", sans-serif; font-style: italic; font-weight: 700;
    font-size: 19px; line-height: 22px; color: var(--white);
    text-shadow: 0 1px 3px rgba(0,0,0,.75);
  }
  .hero__invite span { display: block; font-size: 16px; font-weight: 400; }
  .limited-entry {
    position: absolute; left: 360px; top: 339px; width: 240px; height: 58px;
    border: 2px solid var(--gold-light); border-radius: 3px;
    background: linear-gradient(180deg, #fbe39a 0%, var(--gold) 55%, var(--gold-deep) 100%);
    box-shadow: 0 3px 8px rgba(0,0,0,.45);
    font-size: 25px; font-weight: 400; color: var(--ink);
    display: flex; align-items: center; justify-content: center;
  }
  .hero__note {
    position: absolute; left: 0; right: 0; top: 405px; text-align: center;
    font-size: 12.5px; line-height: 19px; color: var(--ink);
  }

  /* Black band */
  .velvet-band {
    position: absolute; left: 0; top: 461px; width: 960px; height: 182px;
    background: radial-gradient(ellipse at center, #2a2418 0%, var(--band) 60%);
    border-top: 4px solid var(--gold); border-bottom: 4px solid var(--gold);
    text-align: center;
  }
  .velvet-band__title {
    margin-top: 20px; font-family: "Archivo Black", sans-serif; font-size: 66px;
    line-height: 78px; letter-spacing: 1px;
    background: linear-gradient(180deg, #fff8d6 0%, #f1cb63 45%, #b5821d 100%);
    -webkit-background-clip: text; background-clip: text; color: transparent;
  }
  .velvet-band__perk { font-size: 24px; line-height: 32px; color: var(--white); font-weight: 400; }

  /* Offer */
  .offer {
    position: absolute; left: 0; top: 643px; width: 960px; height: 466px;
    background: radial-gradient(ellipse at 50% 20%, #fbfaf5 0%, var(--cream) 75%);
  }
  .offer__headline {
    position: absolute; left: 0; right: 0; top: 12px; text-align: center;
    font-family: "Great Vibes", cursive; font-size: 82px; line-height: 90px; color: var(--ink);
  }
  .offer__exclusive {
    position: absolute; left: 0; right: 0; top: 120px; text-align: center;
    font-size: 23px; color: #222;
  }
  .offer__draw {
    position: absolute; left: 0; right: 0; top: 165px; text-align: center;
    font-family: "Arimo", sans-serif; font-style: italic; font-weight: 700;
    font-size: 14.5px; line-height: 21px; color: var(--ink);
  }
  .tier { position: absolute; top: 242px; width: 310px; text-align: center; }
  .tier--gold { left: 50px; }
  .tier--silver { left: 590px; }
  .tier__name {
    font-family: "Arimo", sans-serif; font-weight: 400; font-size: 28px; line-height: 34px;
    color: var(--ink); text-shadow: 1px 1px 1px rgba(0,0,0,.25);
    padding-bottom: 4px; border-bottom: 3px solid var(--ink); margin-bottom: 10px;
  }
  .tier__text { font-size: 14px; line-height: 20px; color: #222; }
  .bottles {
    position: absolute; left: 395px; top: 937px; width: 176px; height: 263px;
    background: linear-gradient(90deg, #c9c57a 0%, #e6e39c 22%, #5b0f18 30%, #8a1626 48%, #d8d488 55%, #c7c070 72%, #e7a6a0 80%, #f0b8ae 100%);
    border-radius: 14px 14px 0 0; z-index: 2;
  }

  /* Footer */
  .footer {
    position: absolute; left: 0; top: 1109px; width: 960px; height: 91px;
    background: radial-gradient(ellipse at center, #3a2a14 0%, var(--band) 45%);
    color: var(--white); font-size: 12.5px; line-height: 17px;
  }
  .footer__address { position: absolute; left: 66px; top: 22px; }
  .footer__contact { position: absolute; right: 85px; top: 22px; text-align: right; }
</style>
</head>
<body>
<main class="poster">
  <section class="hero">
    <div class="hero__waiter hero__waiter--left" role="img" aria-label="Photograph of a waiter in a dinner suit holding a silver tray with a glass of red wine"></div>
    <div class="hero__waiter hero__waiter--right" role="img" aria-label="Photograph of a waiter in a dinner suit holding a silver tray with a glass of red wine"></div>
    <h1 class="brand"><span class="brand__mark"></span>Ortel Ridge</h1>
    <p class="hero__invite">We Want You to Become Part of Our Story.<span>Join the Ortel Wine Club to get the<br>most out of the wines you love.</span></p>
    <div class="limited-entry">LIMITED ENTRY</div>
    <p class="hero__note">We produce only 1600 cases of wine each vintage.<br>Therefore we have limited membership 001-999 for our club.</p>
  </section>

  <section class="velvet-band">
    <h2 class="velvet-band__title">JOIN THE VELVET ROLL</h2>
    <p class="velvet-band__perk">You will be invited to Velvet Roll Only Events and Tastings</p>
    <p class="velvet-band__perk">You will get Preferential Access to New and Limited Releases</p>
  </section>

  <section class="offer">
    <h2 class="offer__headline">Award Winning Wine</h2>
    <p class="offer__exclusive">Exclusively To You, From Us. Not Available by Other Retailers.</p>
    <p class="offer__draw">**Members will be entered into a bi-annual drawing to win a<br>2 Night Stay here at the Ortel Weavers Lodge on the Freycinet Coast Tasmania!**</p>
    <div class="tier tier--gold">
      <h3 class="tier__name">GOLD MEMBERSHIP</h3>
      <p class="tier__text">We will reserve 2 cases of our limited vintage<br>to be delivered to you in May and October<br>Single varietal or mixed cases.<br>You receive a 15% discount.</p>
    </div>
    <div class="tier tier--silver">
      <h3 class="tier__name">SILVER MEMBERSHIP</h3>
      <p class="tier__text">We will reserve 1 case of our limited<br>vintage to be delivered to you<br>6 bottles in May and 6 in October<br>Single varietal or mixed cases.<br>You receive a 10% discount.</p>
    </div>
  </section>

  <div class="bottles" role="img" aria-label="Photograph of four Ortel Ridge wine bottles: two whites, a red and a rosé"></div>

  <footer class="footer">
    <p class="footer__address">Ortel Ridge<br>Cellar Door: 220 Saltmarsh Road<br>Kelvale Tasmania 7199</p>
    <p class="footer__contact">www.ortelridge-example.com.au<br>Telephone: 0400 555 201 / 0400 555 318</p>
  </footer>
</main>
</body>
</html>
```